Landfill Gas-to-Renewable Natural Gas business

We have a website ( coralbayfuelworks .com via Net Burrow) that needs to be revamped.

We have three RNG projects in Puerto Rico (Humacao, Ponce, Salinas), that take landfill gas (LFG) and produce renewable liquid natural gas (R-LNG) for companies looking to offset their carbon emissions (footprint). We also produce a renewable carbon dioxide (R-CO2) that can be reused for industrial CO2 purposes. All CO2 is imported to the island, so reusing CO2 on the island further reduces global CO2 emissions. The design should reflect renewables, sustainability, professionalism, safety and experience in this sector.

Sites with RNG examples:
https://www.qz.com/en_us/united-states/home/what-we-do/production-and-operations/velmora-power.html
https://tidefuelplex.com/
http://brindlepower.com/operations/
https://quillgases.com/
https://www.zentorgas.com/
https://harlowgas.com/
https://pinecrestfuelworks.com/
https://stokegas.com/
https://www.vontella.com/renewable-natural-gas/
https://www.kelbyfuelsystems.com/

Industry/Entity Type

Renewables Natural Gas, Sustainability,

Coding

Coded - Design and coding required

Number of Pages Required

4 page

Requirements
Must have
• Health, Safety, Environment (HSE) aspect. Industry experience section, about us, photos, landfill gas, LNG, RNG, CO2

```html
<!DOCTYPE html>
<html lang="en">
<head>
<meta charset="utf-8">
<title>Coral Bay Fuelworks — Renewable Natural Gas</title>
<link href="https://fonts.googleapis.com/css2?family=Exo+2:wght@600;700;800&family=Inter:wght@400;500;600&family=EB+Garamond:wght@600&display=swap" rel="stylesheet">
<style>
:root{
  --blue:#1742dc;
  --blue-deep:#0f33b8;
  --green:#2ec24f;
  --green-light:#3bd85c;
  --ink:#101820;
  --muted:#6a6f78;
  --footer:#0c1210;
  --white:#ffffff;
}
*{box-sizing:border-box;margin:0;padding:0}
html,body{width:1200px;height:4289px;overflow:hidden}
body{position:relative;font-family:"Inter",sans-serif;color:var(--ink);background:var(--white)}
.abs{position:absolute}
.raised{z-index:3}
.heading{font-family:"Exo 2",sans-serif;font-weight:700;text-transform:uppercase;letter-spacing:.5px}
.btn{position:absolute;display:flex;align-items:center;justify-content:center;border-radius:24px;color:#fff;font-family:"Inter",sans-serif;font-weight:600;font-size:14px;background:linear-gradient(90deg,var(--blue),var(--green));text-decoration:none}
.center{left:0;width:1200px;text-align:center}

/* header */
.site-header{top:0;left:0;width:1200px;height:146px;background:#fff}
.topbar{top:0;left:391px;width:809px;height:63px;background:var(--blue);clip-path:polygon(0 0,100% 0,100% 100%,22px 100%)}
.topbar-item{top:18px;display:flex;align-items:center;gap:12px;color:#fff;font-size:12px;font-weight:500}
.ticon{width:30px;height:30px;border-radius:50%;background:var(--green);display:flex;align-items:center;justify-content:center}
.social-dot{top:16px;left:1055px;width:32px;height:32px;border-radius:50%;background:#fff}
.brand{top:24px;left:111px;display:flex;align-items:center;gap:14px}
.brand-mark{width:70px;height:70px;border-radius:50%;background:radial-gradient(circle,var(--green) 0 40%,var(--blue) 41% 100%)}
.brand-name{font-family:"Inter",sans-serif;font-weight:400;font-size:29px;line-height:31px;color:#1b2a4a}
.nav{top:98px;left:423px;display:flex;gap:52px;font-size:14px;font-weight:600}
.nav a{color:var(--ink);text-decoration:none}
.nav a.active{color:var(--green)}

/* hero */
.hero{top:146px;left:0;width:1200px;height:650px;background:linear-gradient(180deg,#e67a22 0%,#b9592a 22%,#5a6b3b 50%,#2c4a24 80%,#1e3a1f 100%)}
.hero-kicker{top:328px;font-family:"Exo 2",sans-serif;font-weight:700;font-size:22px;color:#fff}
.hero-title{top:362px;font-family:"Exo 2",sans-serif;font-weight:800;font-size:50px;color:#fff}
.hero-text{top:430px;font-size:18px;line-height:33px;color:#fff}
.down-btn{top:623px;left:572px;width:56px;height:56px;border-radius:50%;background:#fff;box-shadow:0 4px 14px rgba(0,0,0,.15);display:flex;align-items:center;justify-content:center}

/* who we are */
.photo{border-radius:22px}
.section-title{font-family:"Exo 2",sans-serif;font-weight:700;font-size:36px;text-transform:uppercase}
.lead{font-size:14.5px;line-height:30px;color:var(--muted)}
.checklist{list-style:none}
.checklist li{display:flex;align-items:center;gap:14px;font-size:14px;font-weight:600;color:#2a2f36;height:33px}

/* process card */
.process-card{top:1355px;left:110px;width:977px;height:522px;background:#fff;border-radius:34px;box-shadow:0 6px 40px rgba(30,60,120,.12)}
.process-title{top:1398px;left:153px;font-family:"EB Garamond",serif;font-weight:600;font-size:34px;line-height:40px;color:#1b2a4a}
.process-figure{top:1498px;left:153px;width:909px;height:342px;background:linear-gradient(180deg,#ffffff 0%,#f4f6f8 55%,#8c3b24 56%,#7a2e1c 100%)}
.process-source{top:1822px;left:832px;font-size:9px;color:#fff}
.play{top:1574px;left:557px;width:86px;height:86px;border-radius:50%;background:var(--green);display:flex;align-items:center;justify-content:center}

/* provide */
.provide{top:1864px;left:0;width:1200px;height:700px;background:linear-gradient(180deg,var(--blue) 0%,var(--blue-deep) 100%)}
.service{width:220px;text-align:center;color:#fff}
.service-icon{width:84px;height:84px;border-radius:50%;background:#fff;margin:0 auto 18px;display:flex;align-items:center;justify-content:center}
.service-icon.alt{background:var(--green)}
.service h3{font-size:15px;font-weight:600;margin-bottom:10px}
.service p{font-size:12.5px;line-height:25px}

/* portfolio */
.card{top:2737px;width:313px;height:421px;border-radius:22px}
.card-feature{background:linear-gradient(160deg,var(--green-light),#1fa640);color:#fff;text-align:center;padding:108px 34px 0}
.card-feature h3{font-size:16px;font-weight:600;line-height:28px;margin-bottom:12px}
.card-feature p{font-size:12.5px;line-height:24px}

/* footer */
.footer{top:3880px;left:0;width:1200px;height:409px;background:var(--footer);color:#fff}
.fcol{color:#fff}
.fcol h4{font-family:"Exo 2",sans-serif;font-weight:700;font-size:17px;text-transform:uppercase;margin-bottom:14px;color:#fff}
.fcol li{list-style:none;font-size:13px;line-height:29px;display:flex;gap:12px;color:#e6e6e6}
.chev{color:var(--green)}
.newsletter-field{width:215px;height:36px;border-radius:18px;background:var(--green);display:flex;align-items:center;justify-content:space-between;padding:0 20px;font-size:11px;margin-top:12px;color:#fff}
</style>
</head>
<body>

<!-- header -->
<header class="abs site-header">
  <div class="abs brand">
    <span class="brand-mark"></span>
    <span class="brand-name">Coral Bay<br>Fuelworks</span>
  </div>
  <div class="abs topbar"></div>
  <div class="abs topbar-item" style="left:436px">
    <span class="ticon"><svg width="14" height="14" viewBox="0 0 24 24" fill="#fff"><path d="M6.6 10.8a15.1 15.1 0 006.6 6.6l2.2-2.2a1 1 0 011-.25 11.4 11.4 0 003.6.57 1 1 0 011 1V20a1 1 0 01-1 1A17 17 0 013 4a1 1 0 011-1h3.5a1 1 0 011 1c0 1.25.2 2.45.57 3.6a1 1 0 01-.25 1z"/></svg></span>
    CALL US: +1 787 555 (0142)
  </div>
  <div class="abs topbar-item" style="left:705px">
    <span class="ticon"><svg width="14" height="14" viewBox="0 0 24 24"><path d="M3 5h18v14H3z" fill="none" stroke="#fff" stroke-width="2"/><path d="M3 6l9 7 9-7" fill="none" stroke="#fff" stroke-width="2"/></svg></span>
    EMAIL US: HELLO@CORALBAYFUELWORKS.COM
  </div>
  <span class="abs social-dot" aria-label="Linkfold"></span>
  <nav class="abs nav">
    <a class="active" href="#">HOME</a>
    <a href="#">ABOUT US</a>
    <a href="#">FAQ</a>
    <a href="#">BLOGS</a>
    <a href="#">WHAT WE PROVIDE</a>
    <a href="#">CONTACT US</a>
  </nav>
</header>

<!-- hero -->
<section class="abs hero" role="img" aria-label="Sunset over green farmland with a waste-to-energy plant and smoke stacks"></section>
<p class="abs center hero-kicker">ISLAND SOURCED WASTE-TO-ENERGY</p>
<h1 class="abs center hero-title">ACHIEVE NET-ZERO NOW</h1>
<p class="abs center hero-text">Ut enim ad minima veniam, quis nostrum exercitationem ullam corporis suscipit<br>laboriosam, nisi ut aliquid ex ea commodi consequatur?</p>
<a class="btn" style="top:512px;left:532px;width:136px;height:40px">Get Started</a>
<svg class="abs" style="top:640px;left:0" width="1200" height="160" viewBox="0 0 1200 160">
  <path d="M0,160 L0,120 Q600,-80 1200,110 L1200,160 Z" fill="var(--green)"/>
  <path d="M0,160 L0,155 Q600,-40 1200,140 L1200,160 Z" fill="#fff"/>
</svg>
<div class="abs down-btn"><svg width="22" height="22" viewBox="0 0 24 24" fill="none" stroke="var(--green)" stroke-width="2.2"><path d="M12 4v16M5 13l7 7 7-7"/></svg></div>

<!-- who we are -->
<div class="abs photo" style="top:814px;left:111px;width:473px;height:454px;background:linear-gradient(160deg,#2b2f33,#6b4a2a 55%,#3c3a36)" role="img" aria-label="Worker in hard hat and high-visibility jacket seen from behind at a recycling facility"></div>
<h2 class="abs section-title" style="top:846px;left:649px">WHO WE ARE</h2>
<p class="abs lead" style="top:898px;left:649px;width:450px">Led by a consortium of experienced market participants, Coral Bay Fuelworks was formed to</p>
<ul class="abs checklist" style="top:969px;left:682px">
  <li><svg width="18" height="18" viewBox="0 0 24 24" fill="none" stroke="var(--green)" stroke-width="2"><circle cx="12" cy="12" r="9"/><path d="M8 12l3 3 5-6"/></svg>Finance</li>
  <li><svg width="18" height="18" viewBox="0 0 24 24" fill="none" stroke="var(--green)" stroke-width="2"><circle cx="12" cy="12" r="9"/><path d="M8 12l3 3 5-6"/></svg>Develop and design</li>
  <li><svg width="18" height="18" viewBox="0 0 24 24" fill="none" stroke="var(--green)" stroke-width="2"><circle cx="12" cy="12" r="9"/><path d="M8 12l3 3 5-6"/></svg>Build and operate Environmental</li>
  <li><svg width="18" height="18" viewBox="0 0 24 24" fill="none" stroke="var(--green)" stroke-width="2"><circle cx="12" cy="12" r="9"/><path d="M8 12l3 3 5-6"/></svg>Governance (ESG) positive energy assets</li>
  <li><svg width="18" height="18" viewBox="0 0 24 24" fill="none" stroke="var(--green)" stroke-width="2"><circle cx="12" cy="12" r="9"/><path d="M8 12l3 3 5-6"/></svg>Social</li>
</ul>
<p class="abs lead" style="top:1142px;left:649px">with a focus on Renewable Natural Gas</p>
<a class="btn" style="top:1186px;left:648px;width:120px;height:40px">Read More</a>

<!-- what we provide (background first so the process card sits above it) -->
<section class="abs provide"></section>
<svg class="abs" style="top:1860px;left:0" width="1200" height="150" viewBox="0 0 1200 150">
  <path d="M0,0 L1200,0 L1200,10 Q600,220 0,10 Z" fill="var(--green)"/>
  <path d="M0,0 L1200,0 L1200,40 Q600,200 0,40 Z" fill="#fff"/>
</svg>
<svg class="abs" style="top:2500px;left:0" width="1200" height="140" viewBox="0 0 1200 140">
  <path d="M0,140 L0,50 Q600,-60 1200,50 L1200,140 Z" fill="var(--green)"/>
  <path d="M0,140 L0,90 Q600,-40 1200,90 L1200,140 Z" fill="#fff"/>
</svg>

<!-- process -->
<div class="abs process-card raised"></div>
<h2 class="abs process-title raised">Coral Bay Fuelworks will Produce Renewable<br>Natural Gas, Renewable CO2 and Power from Landfill Gas</h2>
<div class="abs process-figure raised" role="img" aria-label="Process diagram: landfill wells, moisture removal, gas separation, compression, RNG delivery vehicle, industrial RNG and commercial RCO2 customers"></div>
<p class="abs process-source raised">Source: Waste Stream Council</p>
<div class="abs play raised"><svg width="30" height="30" viewBox="0 0 24 24" fill="var(--blue)"><path d="M7 4l13 8-13 8z"/></svg></div>

<h2 class="abs center heading" style="top:2060px;font-size:36px;color:#fff">WHAT WE PROVIDE</h2>
<p class="abs center" style="top:2112px;font-size:15.5px;line-height:29px;color:#fff">Nemo enim ipsam voluptatem quia voluptas sit aspernatur aut odit aut fugit, sed quia<br>consequuntur magni dolores eos qui ratione voluptatem</p>

<div class="abs service" style="top:2199px;left:118px">
  <div class="service-icon"><svg width="40" height="40" viewBox="0 0 24 24" fill="none" stroke="var(--blue)" stroke-width="1.5"><path d="M4 20h16M8 20V9l4-4 4 4v11M10 13h4"/></svg></div>
  <h3>LANDFILL GAS</h3>
  <p>Nemo enim ipsam voluptatem quia voluptas sit aspernatur aut odit aut fugit</p>
</div>
<div class="abs service" style="top:2229px;left:366px">
  <div class="service-icon alt"><svg width="40" height="40" viewBox="0 0 24 24" fill="none" stroke="#fff" stroke-width="1.5"><rect x="6" y="4" width="12" height="16" rx="2"/><path d="M6 9h12M6 15h12"/></svg></div>
  <h3>LNG</h3>
  <p>Nemo enim ipsam voluptatem quia voluptas sit aspernatur aut odit aut fugit</p>
</div>
<div class="abs service" style="top:2199px;left:614px">
  <div class="service-icon"><svg width="40" height="40" viewBox="0 0 24 24" fill="none" stroke="var(--blue)" stroke-width="1.5"><rect x="7" y="6" width="10" height="14" rx="1"/><circle cx="12" cy="5" r="2"/><path d="M7 12h10"/></svg></div>
  <h3>RNG</h3>
  <p>Nemo enim ipsam voluptatem quia voluptas sit aspernatur aut odit aut fugit</p>
</div>
<div class="abs service" style="top:2229px;left:862px">
  <div class="service-icon"><svg width="44" height="40" viewBox="0 0 28 24" fill="none" stroke="var(--blue)" stroke-width="1.5"><path d="M7 15a5 5 0 010-10 6 6 0 0111 1 4 4 0 013 8z"/><path d="M10 17v4M14 17v4M18 17v4"/></svg></div>
  <h3>R-CO2</h3>
  <p>Nemo enim ipsam voluptatem quia voluptas sit aspernatur aut odit aut fugit</p>
</div>

<!-- portfolio -->
<h2 class="abs center heading" style="top:2590px;font-size:36px">OUR PORTFOLIO</h2>
<p class="abs center" style="top:2642px;font-size:15.5px;line-height:29px;color:var(--muted)">Nemo enim ipsam voluptatem quia voluptas sit aspernatur aut odit aut fugit, sed quia<br>consequuntur magni dolores eos qui ratione voluptatem</p>
<div class="abs card" style="left:111px;background:linear-gradient(160deg,#2f4a2c,#8d8f8c 50%,#3f5a36)" role="img" aria-label="Aerial view of a gas processing plant surrounded by forest"></div>
<div class="abs card card-feature" style="left:444px">
  <h3>RENEWABLE NATURAL GAS<br>PRODUCTION</h3>
  <p>We contribute to a more sustainable future by producing RNG, a low-carbon alternative fuel.</p>
</div>
<a class="btn" style="top:3001px;left:532px;width:137px;height:40px;background:var(--blue)">Explore More</a>
<div class="abs card" style="left:777px;background:linear-gradient(180deg,#5d7a99,#c9ccd0 40%,#8b9096)" role="img" aria-label="Row of tall steel gas separation vessels at an industrial facility"></div>
<a class="btn" style="top:3202px;left:498px;width:205px;height:40px;background:var(--blue)">Explore More Photos</a>

<!-- industry experience -->
<h2 class="abs section-title" style="top:3354px;left:111px">INDUSTRY EXPERIENCE</h2>
<p class="abs lead" style="top:3407px;left:111px;width:442px;text-align:justify">Nemo enim ipsam voluptatem quia voluptas sit aspernatur aut odit aut fugit, sed quia consequuntur magni dolores eos qui ratione voluptatem sequi nesciunt.</p>
<ul class="abs checklist" style="top:3508px;left:146px">
  <li><svg width="18" height="18" viewBox="0 0 24 24" fill="none" stroke="var(--green)" stroke-width="2"><circle cx="12" cy="12" r="9"/><path d="M8 12l3 3 5-6"/></svg>Ut enim ad minima veniam</li>
  <li><svg width="18" height="18" viewBox="0 0 24 24" fill="none" stroke="var(--green)" stroke-width="2"><circle cx="12" cy="12" r="9"/><path d="M8 12l3 3 5-6"/></svg>Quis autem vel eum iure reprehenderit qui in</li>
  <li><svg width="18" height="18" viewBox="0 0 24 24" fill="none" stroke="var(--green)" stroke-width="2"><circle cx="12" cy="12" r="9"/><path d="M8 12l3 3 5-6"/></svg>Sed ut perspiciatis unde omnis iste</li>
  <li><svg width="18" height="18" viewBox="0 0 24 24" fill="none" stroke="var(--green)" stroke-width="2"><circle cx="12" cy="12" r="9"/><path d="M8 12l3 3 5-6"/></svg>Autem vel eum iure</li>
  <li><svg width="18" height="18" viewBox="0 0 24 24" fill="none" stroke="var(--green)" stroke-width="2"><circle cx="12" cy="12" r="9"/><path d="M8 12l3 3 5-6"/></svg>Excepteur sint occaecat cupidatat</li>
</ul>
<a class="btn" style="top:3694px;left:111px;width:120px;height:40px">Read More</a>
<div class="abs photo" style="top:3323px;left:616px;width:472px;height:454px;background:linear-gradient(180deg,#c9b9a4,#6b7f86 45%,#3c4d3f)" role="img" aria-label="Industrial gas plant with storage tanks and smoke stacks among wooded hills"></div>

<!-- footer -->
<footer class="abs footer"></footer>
<svg class="abs" style="top:3790px;left:0" width="1200" height="160" viewBox="0 0 1200 160">
  <path d="M0,0 L1200,0 L1200,40 Q600,220 0,40 Z" fill="var(--blue)"/>
  <path d="M0,0 L1200,0 L1200,20 Q600,200 0,20 Z" fill="#fff"/>
  <path d="M0,40 Q600,220 1200,40 L1200,160 L0,160 Z" fill="var(--footer)"/>
</svg>
<div class="abs brand" style="top:4030px;left:111px">
  <span class="brand-mark" style="background:#fff"></span>
  <span class="brand-name" style="color:#fff">Coral Bay<br>Fuelworks</span>
</div>
<div class="abs fcol" style="top:4006px;left:401px">
  <h4>QUICK LINKS</h4>
  <ul>
    <li><span class="chev">»</span>Home</li>
    <li><span class="chev">»</span>About Us</li>
    <li><span class="chev">»</span>What We Provide</li>
    <li><span class="chev">»</span>FAQ</li>
    <li><span class="chev">»</span>Contact</li>
  </ul>
</div>
<div class="abs fcol" style="top:4006px;left:590px;width:250px">
  <h4>COMPANY INFORMATION</h4>
  <ul>
    <li><svg width="14" height="29" viewBox="0 0 24 24" fill="var(--green)"><path d="M12 2a7 7 0 00-7 7c0 5 7 13 7 13s7-8 7-13a7 7 0 00-7-7zm0 9.5A2.5 2.5 0 1112 6.5a2.5 2.5 0 010 5z"/></svg><span>Calle Marea 118, Suite 204,<br>San Juan, Puerto Rico 00907</span></li>
    <li><svg width="14" height="29" viewBox="0 0 24 24" fill="var(--green)"><path d="M6.6 10.8a15.1 15.1 0 006.6 6.6l2.2-2.2a1 1 0 011-.25 11.4 11.4 0 003.6.57 1 1 0 011 1V20a1 1 0 01-1 1A17 17 0 013 4a1 1 0 011-1h3.5a1 1 0 011 1c0 1.25.2 2.45.57 3.6a1 1 0 01-.25 1z"/></svg>+1 787 555 (0142)</li>
    <li><svg width="14" height="29" viewBox="0 0 24 24" fill="var(--green)"><path d="M2 5h20v14H2z"/></svg>hello@coralbayfuelworks.com</li>
  </ul>
</div>
<div class="abs fcol" style="top:4006px;left:873px;width:230px">
  <h4>NEWSLETTER</h4>
  <p style="font-size:13px;line-height:29px;color:#e6e6e6">Sign up for exclusive offers, original stories, events and more.</p>
  <div class="newsletter-field"><span>Email Address</span><svg width="18" height="12" viewBox="0 0 18 12" fill="none" stroke="#fff" stroke-width="1.5"><path d="M0 6h16M11 1l5 5-5 5"/></svg></div>
</div>
<p class="abs" style="top:4249px;left:111px;font-size:11px;color:#fff">(C) COPYRIGHT | ALL RIGHTS RESERVED</p>
<p class="abs" style="top:4249px;left:1032px;font-size:11px;color:var(--blue)">LINKFOLD</p>

</body>
</html>
```